Copper Heron Motor Services needs a logo design

I'm after a logo design for a new Female owned automotive repair workshop in the Queanbeyan/Canberra Australia Area.
We offer repairs on all passenger cars, 4wds and light trucks emphasising a strong honest work ethic and a genuine interest in the customer and their vehicles needs. With business details on the front of the card and what we offer on the back.
I would like a design with a phoenix in multiple colours maybe hovering over a flaming wheel or a car with wheels flaming with the phoenix hovering up out of the flames
Target Market(s)
All Vehicle users
Industry/Entity Type
Automotive
Contact Information for Business Card
On the front
Copper Heron Motor
Maree Tolland Owner/ Mechanic 0413527806
email maree@copperheronmotor.com.au
Website www.copperheronmotorworks.com.au
On the back
All Cars, 4WDs, Light trucks, makes and models
Log book servicing
General vehicle servicing
Major vehicle servicing
brake and clutch servicing and repairs
Suspension repairs
cooling systems
All major and minor mechanical repairs
minor electrical rewiring and repairs
Colors
Designer to choose colors to be used in the design.
Look and feel

```html
<!DOCTYPE html>
<html lang="en">
<head>
<meta charset="utf-8">
<title>Copper Heron Motor – Business Card</title>
<link rel="stylesheet" href="https://fonts.googleapis.com/css2?family=Arvo:wght@400;700&family=Courier+Prime&display=swap">
<style>
  :root {
    --backdrop: #e6e6ea;
    --card: #f3f3f1;
    --ink: #1f2a78;
    --ink-soft: #2e3a8c;
    --feather-dark: #1c2460;
    --feather-mid: #4a55a0;
    --flame-red: #d9301a;
    --flame-orange: #f27a1a;
    --flame-yellow: #f7c62a;
    --shadow: rgba(20, 25, 60, 0.18);
  }
  * { box-sizing: border-box; margin: 0; padding: 0; }
  html, body {
    width: 1200px;
    height: 900px;
    overflow: hidden;
    background: var(--backdrop);
  }
  .stage {
    position: relative;
    width: 1200px;
    height: 900px;
  }
  .card {
    position: absolute;
    top: 140px;
    width: 340px;
    height: 600px;
    background: var(--card);
    box-shadow: 0 8px 24px var(--shadow);
    color: var(--ink);
  }
  .card--back { left: 230px; }
  .card--front { left: 630px; }

  /* Back: services list */
  .services {
    list-style: none;
    padding: 26px 24px 0 26px;
    font-family: "Courier Prime", monospace;
    font-size: 15px;
    line-height: 1.1;
    letter-spacing: 0.08em;
    text-transform: uppercase;
  }
  .services li { margin-bottom: 14px; }

  .back-brand {
    position: absolute;
    left: 26px;
    bottom: 30px;
    right: 20px;
    height: 200px;
  }
  .wordmark {
    font-family: "Arvo", serif;
    font-weight: 400;
    color: var(--ink);
    letter-spacing: 0.06em;
  }
  .back-brand .wordmark {
    position: absolute;
    left: 0;
    top: 18px;
    font-size: 22px;
    line-height: 1.9;
  }
  .back-brand .artwork {
    position: absolute;
    right: 10px;
    top: 0;
    width: 140px;
    height: 200px;
  }

  /* Front */
  .front-brand {
    padding: 30px 26px 0 26px;
    text-align: center;
  }
  .front-brand .wordmark {
    font-size: 30px;
    line-height: 1.25;
  }
  .card--front .artwork {
    display: block;
    margin: 20px auto 0;
    width: 260px;
    height: 320px;
  }
  .contact {
    position: absolute;
    left: 26px;
    right: 20px;
    bottom: 34px;
  }
  .contact__name {
    font-family: "Arvo", serif;
    font-weight: 700;
    font-size: 25px;
    letter-spacing: 0.12em;
    text-transform: uppercase;
  }
  .contact__role {
    margin-top: 12px;
    font-family: "Arvo", serif;
    font-size: 13px;
    letter-spacing: 0.1em;
    text-transform: uppercase;
  }
  .contact__email {
    margin-top: 10px;
    font-family: "Courier Prime", monospace;
    font-size: 13px;
    letter-spacing: 0.06em;
    text-transform: uppercase;
    color: var(--ink-soft);
  }
</style>
</head>
<body>
<main class="stage">

  <section class="card card--back" aria-label="Card back – services">
    <ul class="services">
      <li>All cars, 4WDs, light trucks, makes and models</li>
      <li>Log book servicing</li>
      <li>General vehicle servicing</li>
      <li>Major vehicle servicing</li>
      <li>Brake and clutch servicing and repairs</li>
      <li>Suspension repairs</li>
      <li>Cooling systems</li>
      <li>All major and minor mechanical repairs</li>
      <li>Minor electrical rewiring and repairs</li>
    </ul>
    <div class="back-brand">
      <p class="wordmark">Copper<br>Heron<br>Motor</p>
      <svg class="artwork" viewBox="0 0 140 200" role="img" aria-label="Illustration of a winged bird rising from a flaming wheel">
        <defs>
          <linearGradient id="artBack" x1="0" y1="0" x2="0.6" y2="1">
            <stop offset="0" stop-color="var(--feather-dark)"/>
            <stop offset="0.55" stop-color="var(--feather-mid)"/>
            <stop offset="0.8" stop-color="var(--flame-orange)"/>
            <stop offset="1" stop-color="var(--flame-yellow)"/>
          </linearGradient>
        </defs>
        <rect width="140" height="200" rx="6" fill="url(#artBack)" opacity="0.85"/>
      </svg>
    </div>
  </section>

  <section class="card card--front" aria-label="Card front – contact details">
    <div class="front-brand">
      <p class="wordmark">Copper Heron<br>Motor</p>
    </div>
    <svg class="artwork" viewBox="0 0 260 320" role="img" aria-label="Illustration of a winged bird rising from a flaming wheel">
      <defs>
        <linearGradient id="artFront" x1="0" y1="0" x2="0.6" y2="1">
          <stop offset="0" stop-color="var(--feather-dark)"/>
          <stop offset="0.55" stop-color="var(--feather-mid)"/>
          <stop offset="0.8" stop-color="var(--flame-orange)"/>
          <stop offset="1" stop-color="var(--flame-yellow)"/>
        </linearGradient>
      </defs>
      <rect width="260" height="320" rx="8" fill="url(#artFront)" opacity="0.85"/>
    </svg>
    <div class="contact">
      <p class="contact__name">Maree Tolland</p>
      <p class="contact__role">Owner/ Mechanic — 0413527806</p>
      <p class="contact__email">maree@copperheronmotor.com.au</p>
    </div>
  </section>

</main>
</body>
</html>
```